Create a Wordpress Design (Delvo)

We need a wordpress design for an established auction and real estate company based in Tennessee. The winning design will incorporate a professional color scheme with company logo in a clean layout. The design needs to consider that this will be developed on a responsive theme. Colors are those that will highlight the logo.
Updates

This client, an older gentleman, wants the site to mimic http://www.pranketbids.example/. If you can adjust you designs with this site in mind - perhaps 3 columns, less color etc. We are trying to get him a concept that he likes and he keeps mentioning this site. Do not copy this site, but keep it in mind while re-doing the concept. Thanks, - auction services -

Industry/Entity Type

Real Estate

Font styles to use
Sans Serif

Colors

Designer to choose colors to be used in the design.

Requirements
Must have
• - Navigation: 1) Home - with auctions as content as seen at http://brindlehammerco.example/ 2) Properties for Sale 3) Auctions 4) Sell Your Property 5) Community Info 6) About Us 7) Contact Us

Color will be those that highlight logo in a professional creative way. Site tagline: "Our Signs are Everywhere". Site will have a slideshow - please use stock real estate image for the initial photo.

Widgets: 1) social media (FB twitter, linked In, Youtube, RSS) 2) News & Events blog, 3) testimonials 4) featured Property widget.

Footer will have contact info (below) smaller company logo, and the association logos attached, and contact info:
Phone: (615) 555-0147
Contacts: Marcy Delane-Ortt
Email: marketing@kentdelvo.example
Address: 14-C Harlow Court W, Murfreesboro, TN 37130

Nice to have
• use and styling of a dropdown menu: Under AUCTIONS, 1) Upcoming 2) Past

```html
<!DOCTYPE html>
<html lang="en">
<head>
<meta charset="utf-8">
<title>Delvo Commercial – Real Estate &amp; Auction Company</title>
<link href="https://fonts.googleapis.com/css2?family=Mulish:wght@400;600;700&display=swap" rel="stylesheet">
<style>
:root{
  --red:#c3121b;
  --nav-red:#c20f17;
  --nav-active:#b3aaa8;
  --teal:#3cb39a;
  --dark-btn:#4b4b4b;
  --panel:#f3f3f3;
  --featured:#aaa1a0;
  --news:#d7d7d7;
  --text:#707070;
  --heading:#333;
  --footer:#3b3b3b;
  --footer-bar:#2e2e2e;
  --rule:#dedede;
}
*{box-sizing:border-box;margin:0;padding:0}
html,body{width:1200px;height:2296px;overflow:hidden}
body{position:relative;background:#fff;font-family:"Mulish",Arial,sans-serif;color:var(--text)}
.abs{position:absolute}
a{color:inherit;text-decoration:none}

/* header */
.brand{left:132px;top:15px;width:148px;height:69px;display:flex;align-items:center;gap:10px}
.brand-dot{width:16px;height:16px;border-radius:50%;background:var(--red)}
.brand-name{font-size:34px;font-weight:700;color:var(--red);letter-spacing:1px}
.search{left:866px;top:34px;width:202px;height:35px;border:1px solid #ddd;display:flex;align-items:center;justify-content:space-between;padding:0 10px 0 14px;font-size:12px;font-style:italic;color:#aaa}
.search-sep{position:absolute;right:42px;top:6px;bottom:6px;width:1px;background:#ddd}

/* nav */
.nav{left:0;top:102px;width:1200px;height:46px;background:var(--nav-red)}
.nav-item{position:absolute;top:0;height:46px;line-height:46px;color:#fff;font-size:12.5px;text-transform:uppercase;font-weight:600}
.nav-item.active{background:var(--nav-active);padding:0 17px}
.dropdown{left:393px;top:148px;width:193px;height:80px;background:var(--nav-active);padding:8px 12px 0}
.dropdown-item{color:#fff;font-size:13px;height:32px;line-height:32px;padding-left:22px;position:relative;border-bottom:1px solid rgba(255,255,255,.35)}
.dropdown-item:last-child{border:0}
.dropdown-item::before{content:"→";position:absolute;left:4px;font-size:11px;color:#e6e6e6}

/* hero */
.hero{left:0;top:148px;width:1200px;height:446px;background:linear-gradient(90deg,#2f4a22 0%,#4c6b3a 18%,#8f8a7c 40%,#b7ab94 55%,#6d6a66 72%,#3f5b2f 100%)}
.hero-title{left:142px;top:310px;font-size:35px;color:#fff;font-weight:600}
.hero-text{left:145px;top:384px;width:590px;font-size:12.5px;line-height:20px;color:#fff}
.hero-dots{left:563px;top:570px;display:flex;gap:6px}
.hero-dots span{width:14px;height:14px;border-radius:50%;background:#bbb}
.hero-dots span:first-child{background:#fff}

/* welcome */
.welcome-title{left:0;top:655px;width:1200px;text-align:center;font-size:27px;color:var(--heading)}
.welcome-title em{font-style:normal;color:var(--red)}
.welcome-text{left:142px;top:712px;width:916px;text-align:center;font-size:12.5px;line-height:24px}

/* auctions */
.auctions{left:130px;width:700px;background:var(--panel)}
.section-title{position:absolute;left:18px;top:22px;font-size:24px;color:var(--heading)}
.section-rule{position:absolute;left:18px;right:18px;top:58px;height:1px;background:var(--rule)}
.circle-arrow{position:absolute;width:24px;height:24px;border-radius:50%;border:2px solid #ccc;color:#bbb;font-size:12px;text-align:center;line-height:20px}
.card{position:absolute;left:18px;width:664px;height:400px}
.card-photo{position:absolute;left:0;top:0;width:320px;height:188px;border:3px solid #fff;outline:1px solid #ccc}
.card-title{position:absolute;left:343px;top:2px;font-size:20px;color:var(--red)}
.card-desc{position:absolute;left:343px;top:35px;width:310px;font-size:12.5px;line-height:22px}
.card-block{position:absolute;left:343px;width:310px;border-top:1px solid var(--rule)}
.card-block h3{font-size:18px;font-weight:400;color:var(--heading);margin:13px 0 8px 3px}
.card-block p{font-size:12px;line-height:24px;margin-left:3px}
.card-block b{color:var(--red);font-weight:600}
.tag-btn{position:absolute;height:43px;width:149px;background:#fff;border:1px solid #ddd;font-size:14px;color:#555;display:flex;align-items:center;padding-left:20px;gap:12px}
.tag-btn svg{width:18px;height:18px}
.wide-btn{position:absolute;top:353px;width:314px;height:46px;font-size:15px;color:#fff;display:flex;align-items:center;justify-content:center;gap:10px}
.wide-btn.location{left:5px;background:var(--dark-btn);justify-content:flex-start;padding-left:28px}
.wide-btn.bid{left:342px;background:var(--teal)}

/* sidebar */
.featured{left:850px;top:839px;width:220px;height:346px;background:var(--featured);color:#fff}
.featured h2{text-align:center;font-size:21px;font-weight:400;margin-top:22px}
.featured-photo{position:absolute;left:15px;top:61px;width:191px;height:125px;border:3px solid #fff;background:linear-gradient(180deg,#7fb1e0 0%,#c9d9e8 50%,#ece9e2 70%,#6a8a46 100%)}
.featured p{position:absolute;left:20px;top:208px;width:185px;font-size:12px;line-height:22px}
.featured-btn{position:absolute;left:27px;top:294px;width:165px;height:34px;background:var(--dark-btn);font-size:12px;text-align:center;line-height:34px}
.news{left:850px;top:1223px;width:220px;height:361px;background:var(--news)}
.news h2{font-size:18px;font-weight:400;color:var(--heading);margin:25px 0 0 24px}
.news-item{position:absolute;left:14px;width:192px;height:96px;border-top:1px solid #c4c4c4;display:flex;padding-top:12px}
.news-date{width:66px;text-align:center}
.news-date strong{display:block;font-size:24px;color:var(--red);font-weight:400;line-height:30px}
.news-date span{font-size:12px;color:#555;border-top:1px solid #bbb;padding-top:2px}
.news-item p{width:120px;font-size:12px;line-height:22px;margin-left:6px}
.testimonial{left:850px;top:1619px;width:220px;height:204px;background:#e8e8e8}
.testimonial h2{font-size:18px;font-weight:400;color:var(--heading);margin:22px 0 0 20px}
.testimonial-rule{position:absolute;left:20px;right:14px;top:56px;height:1px;background:#d2d2d2}
.testimonial blockquote{position:absolute;left:22px;top:64px;width:185px;font-size:12.5px;line-height:22px}
.testimonial blockquote::before{content:"“";font-size:28px;color:#bbb;font-weight:700;margin-right:6px;vertical-align:-8px}
.testimonial cite{position:absolute;left:24px;top:149px;font-style:normal;font-size:12px;color:var(--red);font-weight:600}
.testimonial small{position:absolute;left:24px;top:170px;font-size:12px;font-style:italic;color:#888}

/* associations */
.associations{left:130px;top:1886px;width:940px;height:107px;display:flex;gap:3px}
.assoc{background:#ebebeb;flex:1;display:flex;align-items:center;justify-content:center}
.assoc i{display:block;width:50px;height:46px;background:#2a2a2a;opacity:.85}
.assoc:nth-child(3) i,.assoc:nth-child(6) i{border-radius:50%}
.assoc:nth-child(4) i{border-radius:4px 4px 26px 26px}
.assoc:nth-child(5) i{width:70px;height:30px;border-radius:50%}
.assoc:nth-child(8) i{width:52px;height:54px}

/* footer */
.footer{left:0;top:2046px;width:1200px;height:192px;background:var(--footer);color:#c9c9c9}
.footer-brand{position:absolute;left:132px;top:31px;display:flex;align-items:center;gap:8px}
.footer-brand .brand-dot{width:12px;height:12px}
.footer-brand .brand-name{font-size:28px}
.footer-about{position:absolute;left:134px;top:104px;width:190px;font-size:12.5px;line-height:22px}
.footer-label{position:absolute;left:438px;top:46px;font-size:16px;color:#fff;font-weight:600}
.footer-contact{position:absolute;left:559px;top:49px;font-size:12.5px;line-height:26px}
.footer-contact span{color:var(--teal)}
.footer-address{position:absolute;left:876px;top:51px;font-size:12.5px;line-height:24px}
.footer-address b{color:#fff;font-size:15px;font-weight:600}
.footer-bar{left:0;top:2238px;width:1200px;height:58px;background:var(--footer-bar)}
.copyright{position:absolute;left:135px;top:24px;font-size:11.5px;color:#999}
.social{position:absolute;left:932px;top:13px;display:flex;gap:5px}
.social span{width:31px;height:31px;border-radius:50%;border:2px solid #9a9a9a;background:#555}
</style>
</head>
<body>

<header>
  <a class="abs brand" href="#"><span class="brand-dot"></span><span class="brand-name">Delvo</span></a>
  <div class="abs search">Search here...
    <span class="search-sep"></span>
    <svg width="18" height="18" viewBox="0 0 18 18"><circle cx="7.5" cy="7.5" r="5.5" fill="none" stroke="#555" stroke-width="2"/><line x1="11.5" y1="11.5" x2="16" y2="16" stroke="#555" stroke-width="2.4"/></svg>
  </div>
</header>

<nav class="abs nav">
  <a class="nav-item" style="left:142px" href="#">Home</a>
  <a class="nav-item" style="left:234px" href="#">Properties for Sale</a>
  <a class="nav-item active" style="left:393px" href="#">Auctions</a>
  <a class="nav-item" style="left:517px" href="#">Sell Your Property</a>
  <a class="nav-item" style="left:690px" href="#">Community Info</a>
  <a class="nav-item" style="left:840px" href="#">About Us</a>
  <a class="nav-item" style="left:950px" href="#">Contact Us</a>
</nav>

<section class="abs hero" role="img" aria-label="Photo of a two-storey suburban house with trees around it"></section>
<div class="abs dropdown">
  <div class="dropdown-item">Upcoming</div>
  <div class="dropdown-item">Past</div>
</div>
<h1 class="abs hero-title">Real Estate &amp; Auction Company</h1>
<p class="abs hero-text">Lorem ipsum dolor sit amet, consectetur adipisicing elit, sed do eiusmod tempor incididunt ut labore et dolore magna aliqua. Ut enim ad minim veniam, quis nostrud exercitation ullamco laboris nisi ut aliquip ex ea commodo consequat.</p>
<div class="abs hero-dots"><span></span><span></span><span></span><span></span></div>

<h2 class="abs welcome-title">Welcome to Our Website <em>Mainpage..</em></h2>
<p class="abs welcome-text">Lorem ipsum dolor sit amet, consectetur adipisicing elit, sed do eiusmod tempor incididunt ut labore et dolore magna aliqua. Ut enim ad minim veniam, quis nostrud exercitation ullamco laboris nisi ut aliquip ex ea commodo consequat. Duis aute irure dolor in reprehenderit in voluptate velit esse cillum dolore eu fugiat nulla pariatur. Lorem ipsum dolor sit amet, consectetur adipisicing elit, sed do eiusmod tempor incididunt.</p>

<!-- Latest auctions -->
<section class="abs auctions" style="top:839px;height:508px">
  <h2 class="section-title">Latest Auctions</h2>
  <span class="circle-arrow" style="right:16px;top:20px">›</span>
  <div class="section-rule"></div>
  <article class="card" style="top:81px">
    <div class="card-photo" role="img" aria-label="Photo of a brick family house with a double garage" style="background:linear-gradient(180deg,#3d8be0 0%,#9cc6ef 40%,#8e7566 60%,#6b7a55 100%)"></div>
    <h3 class="card-title">Finibus Bonorum et Malorum</h3>
    <p class="card-desc">Duis aute irure dolor in reprehenderit in voluptate vel esse cillum dolore eu fugiat nulla pariatur dolor sit amet, consectetur adipisicing elit</p>
    <div class="card-block" style="top:115px"><h3>Online Bidding Only</h3><p><b>Begins:</b> Tuesday, May 30, 2017 at 11:00 AM EDT<br><b>Ends:</b> Wednesday, May 31, 2017 at 11:00 AM EDT</p></div>
    <div class="card-block" style="top:225px"><h3>Live Off-Site Auction</h3><p><b>Begins:</b> Tuesday, May 30, 2017 at 11:00 AM EDT<br><b>Ends:</b> Wednesday, May 31, 2017 at 11:00 AM EDT</p></div>
    <a class="tag-btn" style="left:5px;top:214px" href="#"><svg viewBox="0 0 18 18"><rect x="3" y="2" width="12" height="15" fill="#555"/><rect x="6" y="0" width="6" height="4" fill="#555"/></svg>Details ››</a>
    <a class="tag-btn" style="left:172px;top:214px" href="#"><svg viewBox="0 0 18 18"><rect x="1" y="2" width="16" height="14" fill="none" stroke="#555" stroke-width="2"/><path d="M3 14l4-5 3 3 2-2 4 4z" fill="#555"/></svg>Photos ››</a>
    <a class="tag-btn" style="left:5px;top:275px" href="#"><svg viewBox="0 0 18 18"><rect x="1" y="5" width="11" height="9" fill="#555"/><path d="M12 9l5-3v7z" fill="#555"/></svg>Videos ››</a>
    <a class="wide-btn location" href="#"><svg width="14" height="20" viewBox="0 0 14 20"><path d="M7 0a7 7 0 0 1 7 7c0 5-7 13-7 13S0 12 0 7a7 7 0 0 1 7-7z" fill="#fff"/><circle cx="7" cy="7" r="2.5" fill="#4b4b4b"/></svg>P.O. Box 40912 Roanoke, VA 24018</a>
    <a class="wide-btn bid" href="#">Click here for Online Bidding ››</a>
  </article>
</section>

<section class="abs auctions" style="top:1370px;height:456px">
  <article class="card" style="top:31px">
    <div class="card-photo" role="img" aria-label="Photo of a row of suburban houses along a street" style="background:linear-gradient(180deg,#5a96d8 0%,#bcd6ef 40%,#7a6a58 62%,#56606a 100%)"></div>
    <h3 class="card-title">Finibus Bonorum et Malorum</h3>
    <p class="card-desc">Duis aute irure dolor in reprehenderit in voluptate vel esse cillum dolore eu fugiat nulla pariatur dolor sit amet, consectetur adipisicing elit</p>
    <div class="card-block" style="top:115px"><h3>Online Bidding Only</h3><p><b>Begins:</b> Tuesday, May 30, 2017 at 11:00 AM EDT<br><b>Ends:</b> Wednesday, May 31, 2017 at 11:00 AM EDT</p></div>
    <div class="card-block" style="top:225px"><h3>Live Off-Site Auction</h3><p><b>Begins:</b> Tuesday, May 30, 2017 at 11:00 AM EDT<br><b>Ends:</b> Wednesday, May 31, 2017 at 11:00 AM EDT</p></div>
    <a class="tag-btn" style="left:5px;top:214px" href="#"><svg viewBox="0 0 18 18"><rect x="3" y="2" width="12" height="15" fill="#555"/><rect x="6" y="0" width="6" height="4" fill="#555"/></svg>Details ››</a>
    <a class="tag-btn" style="left:172px;top:214px" href="#"><svg viewBox="0 0 18 18"><rect x="1" y="2" width="16" height="14" fill="none" stroke="#555" stroke-width="2"/><path d="M3 14l4-5 3 3 2-2 4 4z" fill="#555"/></svg>Photos ››</a>
    <a class="tag-btn" style="left:5px;top:275px" href="#"><svg viewBox="0 0 18 18"><rect x="1" y="5" width="11" height="9" fill="#555"/><path d="M12 9l5-3v7z" fill="#555"/></svg>Videos ››</a>
    <a class="wide-btn location" href="#"><svg width="14" height="20" viewBox="0 0 14 20"><path d="M7 0a7 7 0 0 1 7 7c0 5-7 13-7 13S0 12 0 7a7 7 0 0 1 7-7z" fill="#fff"/><circle cx="7" cy="7" r="2.5" fill="#4b4b4b"/></svg>P.O. Box 40912 Roanoke, VA 24018</a>
    <a class="wide-btn bid" href="#">Click here for Online Bidding ››</a>
  </article>
</section>

<!-- Sidebar -->
<aside>
  <div class="abs featured">
    <h2>Featured Property</h2>
    <div class="featured-photo" role="img" aria-label="Photo of a white two-storey colonial house"></div>
    <p>Duis aute irure dolor in repreh enderit in voluptate vel esse cillum dolore</p>
    <a class="featured-btn" href="#">More Properties ››</a>
  </div>

  <div class="abs news">
    <h2>News &amp; Events</h2>
    <div class="news-item" style="top:70px;border-top:0"><div class="news-date"><strong>02</strong><span>Aug 2014</span></div><p>Duis aute irure dol in repreh enderit in voluptate vel.</p></div>
    <div class="news-item" style="top:166px"><div class="news-date"><strong>04</strong><span>Aug 2014</span></div><p>Duis aute irure dol in repreh enderit in voluptate vel.</p></div>
    <div class="news-item" style="top:262px"><div class="news-date"><strong>08</strong><span>Aug 2014</span></div><p>Duis aute irure dol in repreh enderit in voluptate vel.</p></div>
  </div>

  <div class="abs testimonial">
    <h2>Testimonial</h2>
    <span class="circle-arrow" style="right:14px;top:20px">›</span>
    <div class="testimonial-rule"></div>
    <blockquote>Duis aute irure dolor in reprehenderit in voluptate vel esse cillum dolore.</blockquote>
    <cite>by Dara Whitlow</cite>
    <small>From Newyork</small>
  </div>
</aside>

<div class="abs associations">
  <div class="assoc"><i></i></div><div class="assoc"><i></i></div><div class="assoc"><i></i></div><div class="assoc"><i></i></div>
  <div class="assoc"><i></i></div><div class="assoc"><i></i></div><div class="assoc"><i></i></div><div class="assoc"><i></i></div>
</div>

<footer class="abs footer">
  <div class="footer-brand"><span class="brand-dot"></span><span class="brand-name">Delvo</span></div>
  <p class="footer-about">Duis aute irure dolor in repreh enderit in voluptate.</p>
  <div class="footer-label">Contact Info :</div>
  <div class="footer-contact">Phone: <span>(615) 555-0147</span><br>Contacts: Marcy Delane-Ortt<br>Email: <span>marketing@kentdelvo.example</span></div>
  <div class="footer-address"><b>Address:</b> 14-C Harlow Court W,<br>Murfreesboro, TN 37130</div>
</footer>
<div class="abs footer-bar">
  <p class="copyright">©2014 Your Site. All right reserved.</p>
  <div class="social"><span></span><span></span><span></span><span></span></div>
</div>

</body>
</html>
```